Harbor-Glow

Letter heads, business cards, packaging envelopes big and small, and stationery
We have logo design and trademarked approval, we would lie to
upload design to help create this project.
This product was created for my Mother a 4 time diganosed Cancer
Survivor, This product has patent pending and now will be offered to the general public as well.
We are looking foward to working with all of you as this product
and stationary will be viewed worldwide.
Thanks
The Penwick Family

all ages and worldwide

Business

Must have
• Our Logo

```html
<!DOCTYPE html>
<html lang="en">
<head>
<meta charset="utf-8">
<title>Harbor-Glow Stationery</title>
<link rel="stylesheet" href="https://fonts.googleapis.com/css2?family=Ubuntu:wght@400;700&display=swap">
<style>
  :root {
    --brand-red: #c4161c;
    --brand-navy: #1d3b86;
    --envelope-flap: #b30000;
    --paper: #ffffff;
    --backdrop: #e9e4dc;
    --ink: #333333;
    --shadow: rgba(0, 0, 0, 0.18);
  }
  * { margin: 0; padding: 0; box-sizing: border-box; }
  html, body {
    width: 1200px;
    height: 1020px;
    overflow: hidden;
    background: var(--backdrop);
    font-family: "Ubuntu", Arial, sans-serif;
  }
  .stationery-set {
    position: relative;
    width: 1200px;
    height: 1020px;
  }
  .envelope {
    position: absolute;
    left: 528px;
    top: 496px;
    width: 660px;
    height: 512px;
    background: var(--paper);
    box-shadow: 0 2px 8px var(--shadow);
  }
  .envelope-flap {
    position: absolute;
    inset: 0;
  }
  .letterhead {
    position: absolute;
    left: 36px;
    top: 26px;
    width: 662px;
    height: 512px;
    background: var(--paper);
    box-shadow: 0 2px 8px var(--shadow);
  }
  .brand {
    position: absolute;
    left: 18px;
    top: 24px;
  }
  .brand-name {
    display: flex;
    align-items: center;
    gap: 7px;
    font-weight: 700;
    font-size: 26px;
    line-height: 1;
    color: var(--brand-red);
  }
  .brand-dot {
    width: 16px;
    height: 16px;
    border-radius: 50%;
    background: var(--brand-red);
  }
  .brand-tagline {
    margin-top: 3px;
    margin-left: 23px;
    font-weight: 700;
    font-size: 11.5px;
    color: var(--brand-navy);
  }
  .contact-block {
    position: absolute;
    left: 0;
    top: 458px;
    padding-left: 17px;
    border-left: 5px solid var(--brand-navy);
    font-style: normal;
    font-size: 8px;
    line-height: 10.5px;
    color: var(--ink);
  }
  .contact-block .label {
    color: var(--brand-red);
    margin-right: 2px;
  }
</style>
</head>
<body>
  <main class="stationery-set">
    <section class="envelope" aria-label="Envelope">
      <svg class="envelope-flap" width="660" height="512" viewBox="0 0 660 512">
        <polygon points="574,14 660,0 660,512 574,502" fill="var(--envelope-flap)"/>
      </svg>
    </section>

    <section class="letterhead" aria-label="Letterhead">
      <header class="brand">
        <div class="brand-name"><span class="brand-dot"></span>Harbor-Glow</div>
        <div class="brand-tagline">Bringing Comfort Close To Home</div>
      </header>

      <address class="contact-block">
        <div><span class="label">a:</span>5345 Any Street west,Townsvile,ST&nbsp; 54321</div>
        <div><span class="label">p:</span>000 000 000 &nbsp;<span class="label">f:</span>000 000 000</div>
        <div><span class="label">e:</span>name@harborglow.com</div>
        <div><span class="label">w:</span>www.harborglow.com</div>
      </address>
    </section>
  </main>
</body>
</html>
```